Verpackungen
Danke für die unkomplizierte Abwicklung!
Zielgruppe
Wir sind ein Lebensmittelhersteller und wollen eine neue Gewürzlinie für hochwertige Gewürze launchen. Hierbei handelt es sich um Gewürze für den Bereich Grillen und Kochen. Unsere Zielgruppe sind Männer sowie Frauen über 20 Jahre. Das Produkt selber soll sehr hochwertig sein, somit soll auch das Design den Premium-Aspekt widerspiegeln.
Die Markenbezeichnung lautet 'Korn & Rauch'.
Aufgabenstellung
Bei dem Projekt handelt es sich um eine Karton Umverpackung (Sekundärverpackung) mit jeweils 4 Runddosen (Primärverpackung)! Die Stanzkontur hängt dem Briefing an.
In der Verpackung sollen 'Mischungen würzender Zutaten' verpackt werden.
Es handelt sich bei der Verpackung um einen Fefco 427 Karton in braun (Kraft) mit EINFARBIGEM Druck auf der Außenseite.
Logodateien sind bereits vorhanden.
Aktuell gibt es 4 verschiedene BBQ Gewürze, die in dem Geschenkset kombiniert werden. Die Bezeichnungen sind:
Donnerkeil, Silberbüffel, Seefahrerbeute und Abendwind. Das Design der Runddosen ist dem Briefing zu entnehmen.
WICHTIGER HINWEIS: Wir haben uns für den braunen und eher unscheinbaren Karton mit einfarbigem Druck entschieden um den Kontrasteffekt beim Öffnen zu verstärken.
Das Design soll einfach aber schick sein. Gerne dürfen Batches verwendet werden (aber kein Muss) wie z.B. 'liebevoll handgemacht', 'schonend verarbeitet', 'regional hergestellt'.
Auf die Verpackung müssen zusätzlich noch folgende Informationen:
1. Mischung würzender Zutaten
2. 4 x 50 g netto
3. Mindestens haltbar bis / Lot Nr.:
4. Recycling Symbol
5. EAN Code
6. KuvaLimo GmbH & Co. KG, Lindtaler Ring 12, 93461 Hasselfurt
Für den EAN Code bitte vorerst einen Platzhalter / Dummy verwenden, der tatsächliche EAN Code wird vor der Dateiübergabe gesendet.

```html
<!DOCTYPE html>
<html lang="de">
<head>
<meta charset="utf-8">
<title>Korn &amp; Rauch – Umverpackung Stanzkontur</title>
<link rel="stylesheet" href="https://fonts.googleapis.com/css2?family=Oswald:wght@500&family=Roboto:wght@400&family=Kaushan+Script&display=swap">
<style>
:root{
  --ink:#000;
  --kraft:#c99f69;
  --gold:#c9a06a;
  --herb-dark:#120e08;
  --herb-gold:#6e5533;
  --cut:#d9d9d9;
  --crease-a:rgba(201,160,106,.9);
  --crease-b:rgba(230,230,230,.75);
  --code:#111;
}
*{margin:0;padding:0;box-sizing:border-box}
html,body{width:1200px;height:1000px;overflow:hidden;background:var(--ink)}
.sheet{position:relative;width:1200px;height:1000px;background:var(--ink);overflow:hidden}
.flutes{position:absolute;top:0;height:1000px;
  background:repeating-linear-gradient(90deg,var(--crease-a) 0 1px,transparent 1px 5px,var(--crease-b) 5px 6px,transparent 6px 11px)}
.flutes--left{left:180px;width:211px}
.flutes--right{left:796px;width:251px}
.dieline{position:absolute;inset:0}
.panel{position:absolute;background:var(--ink)}
.kraft{position:absolute;background:var(--kraft)}
.flip{transform:rotate(180deg)}
.abs{position:absolute;line-height:1}
.condensed{font-family:"Oswald",sans-serif;font-weight:500;color:var(--gold);text-transform:uppercase;letter-spacing:-.2px;white-space:nowrap}
.centered{text-align:center}
.brand{font-family:"Oswald",sans-serif;font-weight:500;color:var(--gold);white-space:nowrap;text-align:center;line-height:1}
.netto{font-family:"Roboto",sans-serif;color:var(--gold);white-space:nowrap;text-align:center;line-height:1}
.ean-number{font-family:"Roboto",sans-serif;color:var(--code);white-space:nowrap;text-align:center;line-height:1;letter-spacing:.5px}
.herbs{position:absolute;left:0;width:405px;height:67px;
  background:linear-gradient(90deg,var(--herb-gold) 0%,var(--herb-dark) 14%,var(--herb-gold) 32%,var(--herb-dark) 46%,var(--herb-gold) 60%,var(--herb-dark) 74%,var(--herb-gold) 90%,var(--herb-dark) 100%)}
.badge{position:absolute;background:var(--kraft);color:var(--code);font-family:"Kaushan Script",cursive;font-size:10px;line-height:1;padding:5px 6px;white-space:nowrap}
.recycle{position:absolute;width:33px;height:33px}
</style>
</head>
<body>
<main class="sheet">
  <div class="flutes flutes--left"></div>
  <div class="flutes flutes--right"></div>

  <svg class="dieline" width="1200" height="1000" viewBox="0 0 1200 1000" fill="none" stroke="var(--cut)" stroke-width="0.8">
    <path d="M310 0 C240 10 192 70 192 120 Q192 135 206 135 L310 135"/>
    <path d="M882 0 C950 10 1004 70 1004 120 Q1004 135 990 135 L882 135"/>
    <path d="M323 142 L230 170 Q186 182 186 215 L186 385 Q186 410 230 420 L290 429 L323 429"/>
    <path d="M873 142 L966 170 Q1011 182 1011 215 L1011 385 Q1011 410 966 420 L906 429 L873 429"/>
    <path d="M310 437 L170 437 L170 560 L300 568 L310 576"/>
    <path d="M886 437 L1026 437 L1026 560 L896 568 L886 576"/>
    <path d="M310 580 L6 580 L6 670 L0 672 M0 765 L6 767 L6 858 L310 858"/>
    <path d="M886 580 L1188 580 L1188 670 L1194 672 M1194 765 L1188 767 L1188 858 L886 858"/>
    <line x1="147" y1="580" x2="147" y2="858"/><line x1="162" y1="580" x2="162" y2="858"/>
    <line x1="1033" y1="580" x2="1033" y2="858"/><line x1="1048" y1="580" x2="1048" y2="858"/>
    <path d="M330 672 L306 672 L306 767 L330 767"/>
    <path d="M866 672 L890 672 L890 767 L866 767"/>
    <path d="M313 866 L170 884 L170 1000 M883 866 L1026 884 L1026 1000"/>
    <rect x="310" y="0" width="486" height="140"/>
    <rect x="391" y="140" width="405" height="292"/>
  </svg>

  <!-- lid tuck panel (printed upside down) -->
  <section class="panel flip" style="left:310px;top:0;width:486px;height:140px">
    <div class="kraft" style="right:0;top:0;width:126px;height:140px">
      <div class="abs ean-number" style="left:0;width:126px;top:90px;font-size:12px">01234567</div>
    </div>
    <div class="abs condensed" style="left:13px;top:10px;font-size:9.7px">Mindestens haltbar bis / Lot Nr.:</div>
    <div class="abs brand" style="left:129px;width:148px;top:48px;font-size:26px">Korn &amp; Rauch</div>
    <div class="abs condensed centered" style="left:135px;width:131px;top:83px;font-size:10.5px">Mischung würzender Zutaten</div>
    <svg class="recycle" style="left:13px;top:83px" viewBox="0 0 34 34" fill="none" stroke="var(--gold)" stroke-width="4" stroke-linecap="round"><path d="M13 8 L8 17 M21 8 L26 17 M23 27 L11 27"/><path d="M17 3 L22 9 L14 10 Z M29 22 L27 29 L22 24 Z M5 22 L12 24 L7 30 Z" fill="var(--gold)" stroke-width="1"/></svg>
  </section>

  <!-- lid top panel (printed upside down) -->
  <section class="panel flip" style="left:391px;top:140px;width:405px;height:292px">
    <div class="herbs" role="img" aria-label="Linienzeichnungen von Thymian, Minze und Blättern mit Adern" style="top:0"></div>
    <div class="herbs" role="img" aria-label="Linienzeichnungen von Blättern mit Adern, Minze und Thymian" style="bottom:0"></div>
    <div class="abs brand" style="left:97px;width:210px;top:93px;font-size:40px">Korn &amp; Rauch</div>
    <div class="abs condensed centered" style="left:106px;width:187px;top:141px;font-size:15px">Mischung würzender Zutaten</div>
    <div class="abs netto" style="left:149px;width:104px;top:174px;font-size:15.5px">4 x 50g NETTO</div>
  </section>
  <div class="badge" style="left:428px;top:222px;transform:rotate(175deg)">liebevoll handgemacht</div>

  <!-- front panel -->
  <section class="panel" style="left:391px;top:432px;width:495px;height:144px">
    <div class="kraft" style="right:0;top:0;width:126px;height:144px">
      <div class="abs ean-number" style="left:0;width:126px;top:92px;font-size:12px">01234567</div>
    </div>
    <div class="abs condensed" style="left:21px;top:10px;font-size:9.7px">Mindestens haltbar bis / Lot Nr.:</div>
    <div class="abs brand" style="left:129px;width:147px;top:46px;font-size:26px">Korn &amp; Rauch</div>
    <div class="abs condensed centered" style="left:136px;width:131px;top:83px;font-size:10.5px">Mischung würzender Zutaten</div>
    <svg class="recycle" style="left:21px;top:84px" viewBox="0 0 34 34" fill="none" stroke="var(--gold)" stroke-width="4" stroke-linecap="round"><path d="M13 8 L8 17 M21 8 L26 17 M23 27 L11 27"/><path d="M17 3 L22 9 L14 10 Z M29 22 L27 29 L22 24 Z M5 22 L12 24 L7 30 Z" fill="var(--gold)" stroke-width="1"/></svg>
  </section>

  <!-- base panel -->
  <section class="kraft" style="left:388px;top:576px;width:406px;height:286px">
    <div class="abs ean-number" style="left:0;width:406px;top:170px;font-size:13px">01234567</div>
  </section>
</main>
</body>
</html>
```